Firma sucht ansprechendes Einfahrtsschild
Zielgruppe
Firmen, sowie Privatpersonen / Laufkundschaft
Aufgabenstellung
Wir suchen für unser Hof ein neues Einfahrtsschild wie z.B. unser selbstversuch Hofschild 3.6.2015 // es hat auch jemand man etwas für uns gemacht vor langer zeit was aber nie benutzt wurde siehe M1 ///
wir suchen mehr etwas was den Leuten auffällt und das wesentliche rüber bringt.

```html
<!DOCTYPE html>
<html lang="de">
<head>
<meta charset="utf-8">
<title>Wäscherei Brenner – Einfahrtsschild</title>
<link href="https://fonts.googleapis.com/css2?family=Roboto+Slab:wght@700&family=Open+Sans:wght@700&display=swap" rel="stylesheet">
<style>
  :root{
    --green:#6cb33f;
    --purple:#4b3b8f;
    --white:#ffffff;
    --photo-light:#f4f6f8;
    --photo-mid:#d9dfe5;
    --photo-dark:#b7c1cb;
  }
  *{margin:0;padding:0;box-sizing:border-box}
  html,body{width:1200px;height:858px;overflow:hidden;background:var(--white)}
  .sign{position:relative;width:1200px;height:858px;overflow:hidden;font-family:"Open Sans",sans-serif}
  .laundry-photo{
    position:absolute;inset:0;
    background:
      radial-gradient(ellipse 420px 520px at 930px 330px, var(--photo-dark) 0%, rgba(183,193,203,0) 70%),
      linear-gradient(90deg, var(--photo-light) 0%, var(--photo-light) 25%, var(--photo-mid) 60%, var(--photo-dark) 100%);
  }
  .brand{
    position:absolute;left:0;top:0;width:550px;height:182px;background:var(--white);
    display:flex;align-items:center;padding-left:44px;
  }
  .brand-name{
    font-family:"Roboto Slab",serif;font-weight:700;font-size:46px;line-height:1;
    color:var(--purple);white-space:nowrap;
  }
  .arrow{position:absolute;left:0;top:0}
  .arrow-label{
    position:absolute;left:270px;top:335px;width:720px;text-align:center;white-space:nowrap;
    font-family:"Roboto Slab",serif;font-weight:700;font-size:124px;line-height:1;color:var(--white);
  }
  .parking{position:absolute;left:50px;top:650px}
  .parking-text{
    position:absolute;left:245px;top:672px;
    font-family:"Roboto Slab",serif;font-weight:700;font-size:50px;line-height:1.2;color:var(--purple);
  }
  .private-badge{position:absolute;left:895px;top:565px}
  .private-text{
    position:absolute;left:895px;top:612px;width:250px;text-align:center;
    font-weight:700;font-size:34px;line-height:1.2;color:var(--white);
  }
</style>
</head>
<body>
<div class="sign">
  <div class="laundry-photo" role="img" aria-label="Foto: lächelnde Person in heller Kleidung an einer Reihe Industriewaschmaschinen in einem Waschsalon"></div>

  <div class="brand">
    <span class="brand-name">Wäscherei Brenner</span>
  </div>

  <svg class="arrow" width="1200" height="858" viewBox="0 0 1200 858" aria-hidden="true">
    <polygon points="44,400 262,218 262,302 1000,302 1000,508 262,508 262,582"
             fill="var(--green)" stroke="var(--white)" stroke-width="4" stroke-linejoin="miter"/>
  </svg>
  <div class="arrow-label">Wäscherei</div>

  <svg class="parking" width="162" height="172" viewBox="0 0 162 172" aria-hidden="true">
    <rect x="0" y="0" width="162" height="172" rx="18" fill="var(--purple)"/>
    <rect x="8" y="8" width="146" height="156" rx="12" fill="none" stroke="var(--white)" stroke-width="5"/>
    <text x="81" y="142" text-anchor="middle" font-family="Open Sans, sans-serif" font-weight="700" font-size="140" fill="var(--white)">P</text>
  </svg>
  <div class="parking-text">Parkplätze<br>im HOF!</div>

  <svg class="private-badge" width="250" height="250" viewBox="0 0 250 250" aria-hidden="true">
    <polygon fill="var(--green)" points="
      125,0 146,47 190,18 186,71 240,70 206,111 250,140 199,155 219,205 167,190 156,243 125,200
      94,243 83,190 31,205 51,155 0,140 44,111 10,70 64,71 60,18 104,47"/>
  </svg>
  <div class="private-text">AUCH<br>FÜR<br>PRIVAT<br>!!!</div>
</div>
</body>
</html>
```